Präsentationsvorlagen für Vorträge
Zielgruppe
Wir machen laborbasierte Selbsttests im Bereich Longevity und bieten dazu auch passende Supplements an
Aufgabenstellung
Ich brauche eine Präsentationsvorlage für Vorträge basierend auf den Farben und Logo in den angehängten Dateien. Soll alles was für Präsentation nötig ist berücksichtigen

```html
<!DOCTYPE html>
<html lang="de">
<head>
<meta charset="utf-8">
<title>Vivarel – Präsentationsvorlagen</title>
<link rel="stylesheet" href="https://fonts.googleapis.com/css2?family=Ubuntu:wght@400;500;700&display=swap">
<style>
  :root {
    --teal: #0d4a45;
    --teal-soft: #155a54;
    --lime: #9dc21c;
    --white: #ffffff;
    --ink: #1d1d1b;
    --frame: #9a9a9a;
  }
  html, body {
    margin: 0;
    padding: 0;
    overflow: hidden;
  }
  body {
    width: 848px;
    height: 1200px;
    background: var(--white);
    position: relative;
    font-family: "Ubuntu", Arial, sans-serif;
    color: var(--ink);
  }
  .slide {
    position: absolute;
    display: block;
    box-shadow: 0 0 0 1px var(--frame);
  }
  .slide-title   { left: 205px; top: 51px;  width: 431px; height: 243px; }
  .slide-light   { left: 51px;  top: 400px; width: 360px; height: 202px; }
  .slide-accent  { left: 430px; top: 454px; width: 362px; height: 204px; }
  .slide-dark    { left: 51px;  top: 831px; width: 360px; height: 202px; }
  .slide-split   { left: 430px; top: 879px; width: 362px; height: 204px; }
  .caption {
    position: absolute;
    left: 0;
    width: 848px;
    text-align: center;
    font-size: 14px;
    color: var(--ink);
  }
  .caption-title  { top: 305px; font-size: 12px; }
  .caption-light  { top: 666px; }
  .caption-dark   { top: 1091px; }
  svg text { font-family: "Ubuntu", Arial, sans-serif; }
</style>
</head>
<body>

<!-- Titelfolie -->
<svg class="slide slide-title" viewBox="0 0 431 243" aria-label="Titelfolie">
  <rect width="431" height="243" fill="var(--teal)"/>
  <path d="M -10 232 C 40 232, 62 215, 70 175 C 80 110, 105 40, 150 -12" fill="none" stroke="var(--lime)" stroke-width="24"/>
  <text x="231" y="166" text-anchor="middle" font-size="36" font-weight="500" fill="var(--white)">Vivarel</text>
  <text x="231" y="185" text-anchor="middle" font-size="14" font-weight="500" fill="var(--lime)">Täglich ein Schritt voraus</text>
</svg>
<div class="caption caption-title">Titelfolie</div>

<!-- Hintergrund hell -->
<svg class="slide slide-light" viewBox="0 0 360 202" aria-label="Folie Hintergrund hell">
  <defs>
    <linearGradient id="jarLight" x1="0" x2="1">
      <stop offset="0" stop-color="#b9bcbb"/>
      <stop offset="0.45" stop-color="#f3f4f3"/>
      <stop offset="1" stop-color="#a9adac"/>
    </linearGradient>
  </defs>
  <rect width="360" height="202" fill="var(--white)"/>
  <text x="10" y="19" font-size="12" font-weight="700" fill="var(--ink)">Unsere Premium-Formeln</text>
  <line x1="6" y1="27" x2="220" y2="27" stroke="var(--lime)" stroke-width="1"/>
  <rect x="0" y="179" width="360" height="23" fill="var(--teal)"/>
  <rect x="17" y="36" width="86" height="150" rx="8" fill="url(#jarLight)" role="img" aria-label="Produktdose Zellkraft Basis"/>
  <text x="110" y="79" font-size="7" font-weight="700" fill="var(--ink)">Zellkraft Basis</text>
  <line x1="110" y1="84" x2="200" y2="84" stroke="var(--ink)" stroke-width="0.6"/>
  <text x="110" y="95" font-size="7" fill="var(--ink)">Produktinfos</text>
  <text x="350" y="194" text-anchor="end" font-size="10" font-weight="500" fill="var(--white)">Vivarel</text>
</svg>

<!-- Hintergrund mit Akzent -->
<svg class="slide slide-accent" viewBox="0 0 362 204" aria-label="Folie mit Akzent">
  <defs>
    <linearGradient id="jarAccent" x1="0" x2="1">
      <stop offset="0" stop-color="#b9bcbb"/>
      <stop offset="0.45" stop-color="#f3f4f3"/>
      <stop offset="1" stop-color="#a9adac"/>
    </linearGradient>
  </defs>
  <rect width="362" height="204" fill="var(--white)"/>
  <path d="M0 0 H130 C 130 60, 90 100, 0 105 Z" fill="var(--lime)"/>
  <text x="10" y="17" font-size="12" font-weight="700" fill="var(--ink)">Unsere Premium-Formeln</text>
  <line x1="6" y1="26" x2="215" y2="26" stroke="var(--lime)" stroke-width="1"/>
  <path d="M250 204 C 280 184, 315 172, 362 168 V204 Z" fill="var(--teal)"/>
  <rect x="17" y="42" width="86" height="150" rx="8" fill="url(#jarAccent)" role="img" aria-label="Produktdose Zellkraft Basis"/>
  <text x="110" y="72" font-size="7" font-weight="700" fill="var(--ink)">Zellkraft Basis</text>
  <line x1="110" y1="77" x2="200" y2="77" stroke="var(--ink)" stroke-width="0.6"/>
  <text x="110" y="90" font-size="7" fill="var(--ink)">Produktinfos</text>
  <text x="352" y="195" text-anchor="end" font-size="10" font-weight="500" fill="var(--white)">Vivarel</text>
</svg>
<div class="caption caption-light">Beispiel Hintergrund hell/mit Akzent</div>

<!-- Hintergrund dunkel -->
<svg class="slide slide-dark" viewBox="0 0 360 202" aria-label="Folie Hintergrund dunkel">
  <rect width="360" height="202" fill="var(--teal)"/>
  <text x="10" y="19" font-size="12" font-weight="700" fill="var(--white)">Wissenschaft &amp; Präzision</text>
  <line x1="6" y1="27" x2="220" y2="27" stroke="var(--lime)" stroke-width="1"/>

  <g class="step step-test">
    <rect x="46" y="56" width="34" height="34" fill="var(--lime)"/>
    <path d="M58 62 H68 M60 62 V71 L53 84 H73 L66 71 V62" fill="none" stroke="var(--white)" stroke-width="1.4" stroke-linejoin="round"/>
    <text x="63" y="110" text-anchor="middle" font-size="10" fill="var(--white)">Test</text>
    <text x="63" y="120" text-anchor="middle" font-size="5.5" fill="var(--white)">Laboranalyse</text>
    <text x="63" y="127" text-anchor="middle" font-size="5.5" fill="var(--white)">ihrer Biomarker</text>
  </g>
  <g class="step step-analyse">
    <rect x="158" y="56" width="34" height="34" fill="var(--lime)"/>
    <path d="M163 61 V85 H188" fill="none" stroke="var(--white)" stroke-width="1.2"/>
    <path d="M165 80 L172 70 L177 76 L186 62" fill="none" stroke="var(--white)" stroke-width="1.4"/>
    <text x="175" y="110" text-anchor="middle" font-size="10" fill="var(--white)">Analyse</text>
    <text x="175" y="120" text-anchor="middle" font-size="5.5" fill="var(--white)">KI-gestützte</text>
    <text x="175" y="127" text-anchor="middle" font-size="5.5" fill="var(--white)">Auswertung</text>
  </g>
  <g class="step step-empfehlung">
    <rect x="261" y="56" width="34" height="34" fill="var(--lime)"/>
    <path d="M263 73 H271 L274 66 L278 81 L282 62 L285 77 L287 73 H293" fill="none" stroke="var(--white)" stroke-width="1.3" stroke-linejoin="round"/>
    <text x="278" y="110" text-anchor="middle" font-size="10" fill="var(--white)">Empfehlung</text>
    <text x="278" y="120" text-anchor="middle" font-size="5.5" fill="var(--white)">Personalisierte</text>
    <text x="278" y="127" text-anchor="middle" font-size="5.5" fill="var(--white)">Supplements</text>
  </g>

  <rect x="0" y="177" width="360" height="13" fill="var(--lime)"/>
  <rect x="0" y="190" width="360" height="12" fill="var(--white)"/>
  <text x="350" y="200" text-anchor="end" font-size="9" font-weight="500" fill="var(--teal)">Vivarel</text>
</svg>

<!-- Hintergrund Akzent geteilt -->
<svg class="slide slide-split" viewBox="0 0 362 204" aria-label="Folie dunkel mit Akzent">
  <rect width="362" height="204" fill="var(--white)"/>
  <path d="M0 0 H240 C 210 50, 195 140, 60 180 H0 Z" fill="var(--teal)"/>
  <text x="10" y="19" font-size="12" font-weight="700" fill="var(--white)">Wissenschaft &amp; Präzision</text>
  <line x1="6" y1="27" x2="232" y2="27" stroke="var(--lime)" stroke-width="1"/>

  <g class="dna-icon" fill="none" stroke="var(--white)" stroke-width="1.2">
    <path d="M14 62 C 22 50, 30 70, 38 58"/>
    <path d="M14 58 C 22 70, 30 50, 38 62"/>
    <path d="M18 57 V63 M24 59 V61 M30 59 V61 M35 57 V63"/>
  </g>
  <text x="10" y="88" font-size="10" fill="var(--white)">Wissenschaft trifft</text>
  <text x="10" y="100" font-size="10" fill="var(--white)">Lebensqualität</text>
  <text x="10" y="113" font-size="4.6" fill="var(--white)">Vivarel kombiniert moderne Labordiagnostik</text>
  <text x="10" y="119" font-size="4.6" fill="var(--white)">mit wissenschaftlich fundierten Nährstoffformeln.</text>
  <text x="10" y="125" font-size="4.6" fill="var(--white)">Unser Ziel: messbare Verbesserungen Ihrer</text>
  <text x="10" y="131" font-size="4.6" fill="var(--white)">Zellfunktion und Lebensqualität.</text>

  <rect x="0" y="180" width="362" height="12" fill="var(--lime)"/>
  <text x="352" y="201" text-anchor="end" font-size="9" font-weight="500" fill="var(--teal)">Vivarel</text>
</svg>
<div class="caption caption-dark">Beispiel Hintergrund dunkel/Akzent</div>

</body>
</html>
```